Stage Design Company Business Card

We are looking to step up up our business card design for our team.

We are a Full service Design and Consultation company for Stage and TV with an emphasis in Theatrical Lighting.

We like our materials to be clean and modern with solid colors free of patterns and gradients. Our brand consists of 4 primary colors Purple, Black, Grey, and White. Provided is our Word Mark as well as our Symbol Logo.

We would like our cards to leave an impression beyond the information, show our attention to design and detail, and make our marks an easily recognized feature (together or apart) for our clients.

We need a warm approachable comfortable feel for some clients, and a professional flair for the board member type clients.

Attached are our brand elements, and our existing cards to give a sense of our style and a glipse at the information we provide on our cards.

Target Market(s)

broad client base from church leaders to high school teachers and architects.

Industry/Entity Type

Business

Contact Information for Business Card

We format our phone number with periods not parenthesis or dashes. Information will be edited for each of our team members, and team member specific cards are not part of this scope, but rather a template so to speak.

Font styles to use
Sans Serif

Colors
6b449b
ffffff
000000
333333
aaaaaa

Requirements
Must have
• Wordmark and logo mark present (does not need to exist on the same side of card)
• Brand Colors,
• Name, Phone, Email, Address.
• Unique choices that make someone stop and take a second look
Nice to have
• It would be nice to somehow convey what we DO, as our brand name does not lend itself to this, outside of an obvious tagline though.....
• social media if not crowded. all of our handles match (instagram, twitter, facebook)
Should not have
• "clipart"

```html
<!DOCTYPE html>
<html lang="en">
<head>
<meta charset="utf-8">
<title>Halvern Stageworks — Business Card</title>
<link rel="stylesheet" href="https://fonts.googleapis.com/css2?family=Source+Sans+3:wght@400;600&display=swap">
<style>
  :root {
    --backdrop: #5f5f5f;
    --brand-purple: #33006b;
    --paper: #ffffff;
    --ink: #000000;
    --ink-soft: #333333;
    --rule: #aaaaaa;
    --muted: #777777;
  }
  * { box-sizing: border-box; margin: 0; padding: 0; }
  html, body { width: 1200px; height: 1200px; overflow: hidden; }
  body {
    background: var(--backdrop);
    font-family: "Source Sans 3", sans-serif;
    display: flex;
    flex-direction: column;
    align-items: center;
    justify-content: center;
    gap: 44px;
  }
  .card {
    position: relative;
    width: 880px;
    height: 499px;
  }
  .card--front { background: var(--paper); color: var(--ink); }
  .card--back { background: var(--brand-purple); color: var(--paper); }

  .brand-name {
    font-weight: 600;
    font-size: 38px;
    letter-spacing: 0.42em;
    white-space: nowrap;
    line-height: 1;
  }
  .card--front .brand-name {
    position: absolute;
    top: 148px;
    left: 0;
    right: 0;
    text-align: center;
    padding-left: 0.42em;
  }

  .identity {
    position: absolute;
    top: 368px;
    left: 0;
    right: 0;
    display: flex;
    justify-content: center;
  }
  .person {
    text-align: right;
    padding-right: 26px;
    border-right: 1px solid var(--rule);
    width: 420px;
    padding-top: 4px;
    padding-bottom: 14px;
  }
  .person__name {
    font-size: 40px;
    font-weight: 400;
    letter-spacing: -0.01em;
    line-height: 1.05;
    color: var(--ink);
  }
  .person__title {
    font-size: 23px;
    color: var(--muted);
    margin-top: 6px;
  }
  .contact-list {
    list-style: none;
    padding-left: 30px;
    width: 420px;
    padding-top: 10px;
  }
  .contact-list li {
    display: flex;
    align-items: center;
    gap: 12px;
    font-size: 27px;
    line-height: 1.28;
    color: var(--ink-soft);
  }
  .icon { width: 22px; height: 22px; flex: none; }
  .card--front .icon { color: var(--brand-purple); }
  .card--back .icon { color: var(--paper); }

  .lockup {
    position: absolute;
    top: 130px;
    left: 0;
    right: 0;
    display: flex;
    align-items: center;
    justify-content: center;
    gap: 34px;
  }
  .lockup__mark {
    width: 120px;
    height: 120px;
    border-radius: 50%;
    background: var(--paper);
  }
  .card--back .brand-name { color: var(--paper); }

  .studio-details {
    position: absolute;
    top: 350px;
    left: 0;
    right: 0;
    text-align: center;
    font-size: 27px;
    line-height: 1.4;
  }
  .studio-details__row {
    display: flex;
    justify-content: center;
    gap: 44px;
  }
  .studio-details__row span {
    display: inline-flex;
    align-items: center;
    gap: 10px;
  }
</style>
</head>
<body>

  <section class="card card--front" aria-label="Card front">
    <div class="brand-name">HALVERN STAGEWORKS</div>
    <div class="identity">
      <div class="person">
        <div class="person__name">Milo R Halvern</div>
        <div class="person__title">Job Title</div>
      </div>
      <ul class="contact-list">
        <li>
          <svg class="icon" viewBox="0 0 24 24" fill="none" stroke="currentColor" stroke-width="2.4"><rect x="6" y="1.5" width="12" height="21" rx="2"/><line x1="10" y1="19" x2="14" y2="19"/></svg>
          000.000.0000
        </li>
        <li>
          <svg class="icon" viewBox="0 0 24 24"><rect x="1" y="5" width="22" height="14" fill="currentColor"/><path d="M1 5 L12 13 L23 5" fill="none" stroke="#fff" stroke-width="1.6"/></svg>
          milo@halvern-s.com
        </li>
      </ul>
    </div>
  </section>

  <section class="card card--back" aria-label="Card back">
    <div class="lockup">
      <div class="lockup__mark"></div>
      <div class="brand-name">HALVERN STAGEWORKS</div>
    </div>
    <div class="studio-details">
      <div>52 N Elm Ave, Tempe, AZ 85281</div>
      <div class="studio-details__row">
        <span>
          <svg class="icon" viewBox="0 0 24 24"><path fill="currentColor" d="M7 2c1 0 2 2.5 2.5 4 .3 1-.8 1.8-1.3 2.4.8 2.6 2.7 5.5 5 7 .7-.4 1.6-1.4 2.6-1 1.4.6 3.7 1.8 3.7 2.8 0 1.5-2 3.8-3.8 3.8C9 21 3 12 3 6.5 3 4.5 5.5 2 7 2z"/></svg>
          555.014.7720
        </span>
        <span>
          <svg class="icon" viewBox="0 0 24 24" fill="none" stroke="currentColor" stroke-width="1.8"><circle cx="12" cy="12" r="10"/><ellipse cx="12" cy="12" rx="4.5" ry="10"/><line x1="2" y1="12" x2="22" y2="12"/><path d="M4 7h16M4 17h16"/></svg>
          halvern-s.com
        </span>
      </div>
    </div>
  </section>

</body>
</html>
```